Marcus Pellow Carpentry & Joinery

Hello, I would like a flyer designed for my new business doing small projects in my local area for home-owners. I am a professional tradesman.
The type of work I am offering is:
- decks/decking
- external stairs & railings
- install windows & doors
- roofs & gutters
- small additions
- built-in wardrobes
- finish work
- demolition

It would be great if the flyer could mention these, or use phrasing that fits this kind of construction work.
My idea for a slogan was "new work and repairs to any age home".

Please also mention FREE QUOTES and have my email and phone number included on the flyer, along with my carpentry licence number, which I can provided.

I'd like a one page, single-sided flyer that could be printed as DL.
Colour and style is up to you! I'll be placing this flyer on counters & in the windows of local businesses, so something simple and eye-catching is preferred.

Thank you!

```html
<!DOCTYPE html>
<html lang="en">
<head>
<meta charset="utf-8">
<title>Marcus Pellow Carpentry &amp; Joinery – Flyer</title>
<link rel="stylesheet" href="https://fonts.googleapis.com/css2?family=Oswald:wght@500;600;700&family=Open+Sans:wdth,wght@75..100,400..800&display=swap">
<style>
  :root {
    --navy: #1c4f95;
    --brick: #a42a14;
    --cream: #f8f3e2;
    --ink: #1a1a1a;
    --grey-text: #565656;
    --link-blue: #1f63b3;
    --white: #ffffff;
  }
  * { margin: 0; padding: 0; box-sizing: border-box; }
  html, body { width: 1200px; height: 607px; overflow: hidden; background: var(--cream); }
  .flyer {
    position: relative;
    width: 1200px;
    height: 607px;
    background: var(--cream);
    font-family: "Open Sans", Arial, sans-serif;
    color: var(--ink);
    overflow: hidden;
  }
  .header-band { position: absolute; inset: 0 0 auto 0; width: 1200px; height: 210px; }
  .headline {
    position: absolute;
    top: 42px; left: 0; width: 1200px;
    text-align: center;
    font-family: "Oswald", "Arial Narrow", sans-serif;
    font-weight: 700;
    font-size: 52px;
    line-height: 1;
    color: var(--white);
    letter-spacing: 0.2px;
  }
  .brand {
    position: absolute;
    top: 244px; left: 62px; width: 352px;
    text-align: center;
    white-space: nowrap;
  }
  .brand-name {
    display: block;
    font-family: "Oswald", "Arial Narrow", sans-serif;
    font-weight: 600;
    font-size: 46px;
    line-height: 56px;
    color: var(--navy);
    text-transform: uppercase;
  }
  .brand-trade {
    display: block;
    margin-top: 8px;
    font-family: "Open Sans", Arial, sans-serif;
    font-weight: 400;
    font-size: 24px;
    line-height: 30px;
    color: var(--ink);
    text-transform: uppercase;
  }
  .intro {
    position: absolute;
    top: 375px; left: 70px; width: 345px;
    font-stretch: 78%;
    font-weight: 700;
    font-size: 18.5px;
    line-height: 22px;
    color: var(--grey-text);
  }
  .intro-brand { color: var(--link-blue); text-transform: uppercase; }
  .services { position: absolute; top: 146px; left: 468px; width: 300px; }
  .services-title { font-weight: 700; font-size: 19px; color: var(--brick); line-height: 24px; }
  .services-list { list-style: none; margin-top: 2px; }
  .services-list li { font-size: 19.5px; line-height: 26px; color: var(--ink); }
  .services-list li::before {
    content: "";
    display: inline-block;
    width: 8px; height: 8px;
    border-radius: 50%;
    background: var(--link-blue);
    margin: 0 8px 3px 1px;
    vertical-align: middle;
  }
  .contact { position: absolute; top: 396px; left: 438px; width: 322px; text-align: center; }
  .call-cta {
    font-stretch: 80%;
    font-weight: 800;
    font-size: 22px;
    line-height: 26px;
  }
  .phone-box {
    margin-top: 6px;
    height: 53px;
    background: var(--brick);
    display: flex;
    align-items: center;
    justify-content: center;
    gap: 10px;
    color: var(--white);
  }
  .phone-icon { width: 36px; height: 36px; }
  .phone-number {
    font-stretch: 80%;
    font-weight: 700;
    font-size: 41px;
    line-height: 1;
  }
  .email-lead { margin-top: 10px; font-size: 19px; line-height: 22px; }
  .email { font-weight: 700; font-size: 19px; line-height: 24px; color: var(--link-blue); }
  .licence { margin-top: 4px; font-size: 17px; line-height: 22px; }
  .gallery { position: absolute; left: 777px; top: 128px; width: 389px; height: 443px; }
  .photo { position: absolute; width: 193px; }
  .photo-deck { left: 0; top: 0; height: 146px; background: linear-gradient(160deg, #8aa36a, #9a6a45 70%, #7a5236); }
  .photo-stairs { left: 196px; top: 0; height: 146px; background: linear-gradient(150deg, #6c7f3e, #d8c7b0 55%, #a58b6d); }
  .photo-windows { left: 0; top: 150px; height: 144px; background: linear-gradient(135deg, #dcdcd2, #b8b6a4 60%, #8c8070); }
  .photo-roof { left: 196px; top: 150px; height: 144px; background: linear-gradient(160deg, #b09072, #8c5a3e 55%, #c9b091); }
  .photo-wardrobe { left: 0; top: 298px; height: 145px; background: linear-gradient(135deg, #4a3a2c, #b38b5c 50%, #6a4a30); }
  .photo-demolition { left: 196px; top: 298px; height: 145px; background: linear-gradient(170deg, #6f9ed6, #b5c7d8 50%, #8a6e4e); }
</style>
</head>
<body>
<main class="flyer">
  <svg class="header-band" viewBox="0 0 1200 210" aria-hidden="true">
    <path d="M0 0 H1200 V126 C820 100 330 112 0 206 Z" fill="var(--brick)"/>
    <path d="M0 0 H1200 V117 C820 91 330 100 0 195 Z" fill="var(--navy)"/>
  </svg>

  <h1 class="headline">New construction or repair to houses of any age</h1>

  <div class="brand">
    <span class="brand-name">Marcus Pellow</span>
    <span class="brand-trade">Carpentry &amp; Joinery</span>
  </div>

  <p class="intro">If you are looking for a highly experienced carpentry and joinery service in the (state your area) and surrounding area, <span class="intro-brand">Marcus Pellow Carpentry &amp; Joinery</span> offers a professional domestic joinery service, with outstanding craftsmanship and exceptional customer service.</p>

  <section class="services">
    <h2 class="services-title">Our services include:</h2>
    <ul class="services-list">
      <li>Deck building</li>
      <li>External stairs &amp; railings</li>
      <li>Windows/doors installation</li>
      <li>Roofs &amp; gutters</li>
      <li>Small additions</li>
      <li>Built-in wardrobes</li>
      <li>Finishing works</li>
      <li>Demolition</li>
    </ul>
  </section>

  <section class="contact">
    <p class="call-cta">Call Now For a Free Quotation</p>
    <div class="phone-box">
      <svg class="phone-icon" viewBox="0 0 36 36" aria-hidden="true">
        <circle cx="18" cy="18" r="16" fill="none" stroke="var(--white)" stroke-width="2.5"/>
        <path d="M12.5 9.5 c1.2-1 2.6-.8 3.2.4 l1.5 3 c.5 1-.1 1.8-.9 2.4 l-1 .7 c.9 2.4 2.4 4.2 4.6 5.4 l.8-.9 c.7-.8 1.6-1.2 2.5-.6 l2.8 1.8 c1.1.7 1.1 2.1.1 3.1 l-1.3 1.2 c-1.6 1.4-4.5.8-7.6-1.6 c-3.6-2.9-6.3-7.1-6.6-10.3 c-.1-1.6.5-3 1.5-3.9 Z" fill="var(--white)"/>
      </svg>
      <span class="phone-number">555.204.7316</span>
    </div>
    <p class="email-lead">or email at</p>
    <p class="email">marcuspellow@mailbox.net</p>
    <p class="licence">LIC. NO, 4821-93056174</p>
  </section>

  <div class="gallery">
    <div class="photo photo-deck" role="img" aria-label="Photo of a timber backyard deck built around a tree"></div>
    <div class="photo photo-stairs" role="img" aria-label="Photo of external stairs with dark railings"></div>
    <div class="photo photo-windows" role="img" aria-label="Photo of a bright room with arched windows and French doors"></div>
    <div class="photo photo-roof" role="img" aria-label="Photo of a tradesman working on a timber roof"></div>
    <div class="photo photo-wardrobe" role="img" aria-label="Photo of lit built-in wardrobes with shelves and hanging space"></div>
    <div class="photo photo-demolition" role="img" aria-label="Photo of an excavator demolishing an old house"></div>
  </div>
</main>
</body>
</html>
```